Stationery Design Project - Mark Velloran

I have recently designed my personal logo - Mark Velloran (here on pixelforum.net) and now i'm looking to complete my corporate identity, with adding:
- Business Card
- Letter Head
- Envelope
- Brochure template (that will be used to promote any of the workshops or other services I provide along with a short summary about my credentials, and testimonials) - you can take your pick from the website: http://markvelloran.example

Refer to website for more insight into the brand and the look & feel

PS.
- PLEASE REFER TO ATTACHED FILE AND READ THE "SHOULD NOT HAVE SECTION OF THIS BRIEF"
- I have attached two vector files, displaying the logo alteration on two different backgrounds (dark & light)
Updates

Target Market(s)

1) One-on-one Business Executive 2) Companies requesting my workshops for mid management teams & public speaking events like KIV Sessions

Industry/Entity Type

Business

Requirements
Must have
• - must fit the look and feel of the logo (notice that I have attached the logo, and an emblem)
- the final files should be ready for printing - with info on colours, sizes, bleed area, margins, UV spot (if applicable), suggested material to print on (applies to business cards in particular)
- brand guide lines should be laid out too (font, colour, etc ...)
Nice to have
• It would be nice to produce something different that your standard sizes & di-cut in terms of business card, and letter head ...
Should not have
• THE EMBLEM (MV) AND THE LOGO (MARK VELLORAN) SHOULD NOT BE LAYED OUT AS PER THE ATTACHED FILE - THEY SHOULD BE SEPARATED - THE EMBLEM (MV) CAN BE USED IN PARTIAL OR AS WATERMARK - BUT NOT THE LOGO (MARK VELLORAN)

```html
<!DOCTYPE html>
<html lang="en">
<head>
<meta charset="utf-8">
<title>Mark Velloran – Letter Envelope</title>
<link rel="stylesheet" href="https://fonts.googleapis.com/css2?family=Didact+Gothic&display=swap">
<style>
  :root {
    --ink: #23232f;
    --paper: #ffffff;
    --brand-blue: #4dbfec;
    --pale-blue: #b9e2f7;
    --stage-light: #f2f2f2;
    --stage-dark: #a8a8a8;
    --line: #8a8a8a;
    --rule: #c9cbd3;
    --text-dark: #2b2b2b;
  }
  * { margin: 0; padding: 0; box-sizing: border-box; }
  html, body { width: 1200px; height: 842px; overflow: hidden; }
  body {
    position: relative;
    background: var(--ink);
    font-family: "Didact Gothic", "Century Gothic", sans-serif;
    color: var(--paper);
  }
  .header { position: absolute; left: 0; top: 0; width: 1200px; height: 232px; background: var(--ink); }
  .header-rule { position: absolute; left: 16px; top: 101px; width: 1184px; height: 1px; background: var(--rule); }
  .page-marker { position: absolute; left: 541px; top: 90px; width: 16px; height: 11px; background: var(--brand-blue); }
  .page-number { position: absolute; left: 541px; top: 102px; font-size: 12px; color: var(--rule); letter-spacing: 0.5px; }
  .section-label { position: absolute; left: 1018px; top: 52px; font-size: 19px; line-height: 18px; letter-spacing: 1px; }
  .page-title { position: absolute; left: 175px; top: 126px; font-size: 41px; line-height: 37px; letter-spacing: 3px; font-weight: 400; }
  .stage {
    position: absolute; left: 16px; top: 232px; width: 1184px; height: 526px;
    background: radial-gradient(ellipse 700px 420px at 50% 50%, var(--stage-light) 0%, #d8d8d8 55%, var(--stage-dark) 100%);
  }
  .letterhead { position: absolute; left: 98px; top: 315px; width: 232px; height: 337px; background: var(--paper); overflow: hidden; }
  .letterhead-art {
    position: absolute; left: 0; top: 110px; width: 175px; height: 227px;
    background: linear-gradient(135deg, #d6d6d6 0%, #c2c2c2 40%, var(--pale-blue) 70%, #ececec 100%);
    border-radius: 0 170px 0 0;
  }
  .letterhead-contact {
    position: absolute; left: 98px; top: 300px;
    font-size: 3.8px; line-height: 5px; color: var(--text-dark); white-space: nowrap;
  }
  .letterhead-contact .row { margin-top: 3px; font-size: 4.2px; }
  .size-note { position: absolute; left: 258px; top: 663px; font-size: 15px; color: var(--text-dark); letter-spacing: 0.5px; }
  .envelopes { position: absolute; left: 0; top: 0; width: 1200px; height: 842px; }
  .palette-title { position: absolute; left: 944px; top: 322px; font-size: 17px; color: var(--text-dark); letter-spacing: 1px; }
  .swatch { position: absolute; left: 944px; width: 201px; height: 20px; font-size: 16px; line-height: 20px; padding-left: 28px; letter-spacing: 0.5px; white-space: nowrap; }
  .swatch-white { top: 356px; background: var(--paper); color: var(--text-dark); }
  .swatch-black { top: 396px; background: #2a2222; color: var(--paper); }
  .swatch-blue { top: 433px; background: var(--brand-blue); color: var(--paper); }
  .font-note { position: absolute; left: 943px; top: 562px; font-size: 18px; color: var(--text-dark); letter-spacing: 0.5px; }
  .footer { position: absolute; left: 0; top: 758px; width: 1200px; height: 84px; background: var(--ink); }
  .footer-name { position: absolute; left: 944px; top: 786px; font-size: 30px; line-height: 30px; white-space: nowrap; }
</style>
</head>
<body>
  <header class="header">
    <div class="header-rule"></div>
    <div class="page-marker"></div>
    <div class="page-number">02</div>
    <div class="section-label">Office<br>Element</div>
    <h1 class="page-title">Letter<br>Envelope</h1>
  </header>

  <main class="stage"></main>

  <section class="letterhead">
    <div class="letterhead-art" role="img" aria-label="Faint partial emblem watermark with a pale blue standing figure"></div>
    <div class="letterhead-contact">
      Norvale Textiles Co., Ltd. Hangzhou<br>
      No.18 2F Lanting Road, Binjiang District, Hangzhou City,<br>
      Zhejiang Prov. China 310000
      <div class="row">☎ 0571-80041270 / ▯ 0571-80041271 / ✉ office@norvale.example</div>
    </div>
  </section>
  <div class="size-note">13*19cm</div>

  <svg class="envelopes" viewBox="0 0 1200 842" aria-label="Envelope front and back">
    <g class="envelope-front" stroke="var(--line)" stroke-width="0.8">
      <path d="M388 424 L374 427 Q372 428 372 431 L372 520 Q372 523 375 523 L388 526 Z" fill="var(--paper)"/>
      <path d="M597 424 L610 427 Q612 428 612 431 L612 520 Q612 523 609 523 L597 526 Z" fill="var(--paper)"/>
      <path d="M388 424 L597 424 L597 526 L594 604 Q594 612 586 612 L398 612 Q390 612 390 604 L388 526 Z" fill="var(--paper)"/>
      <path d="M388 424 L392 386 Q393 377 402 377 L583 377 Q592 377 593 386 L597 424 Z" fill="var(--brand-blue)" stroke="none"/>
      <line x1="388" y1="526" x2="597" y2="526"/>
      <g fill="none" stroke="#333" stroke-width="0.7">
        <rect x="398" y="432" width="8" height="9"/><rect x="408" y="432" width="8" height="9"/>
        <rect x="418" y="432" width="8" height="9"/><rect x="428" y="432" width="8" height="9"/>
        <rect x="438" y="432" width="8" height="9"/><rect x="448" y="432" width="8" height="9"/>
        <rect x="546" y="430" width="20" height="20"/><rect x="566" y="430" width="18" height="20"/>
      </g>
    </g>
    <text class="envelope-name" x="398" y="516" font-size="13" textLength="97" lengthAdjust="spacingAndGlyphs" fill="var(--text-dark)" font-family="Didact Gothic, sans-serif">MARK VELLORAN</text>
    <g transform="rotate(180 460 549)" font-size="3.8" fill="var(--text-dark)" font-family="Didact Gothic, sans-serif">
      <text x="398" y="543">Norvale Textiles Co., Ltd. Hangzhou</text>
      <text x="398" y="548">No.18 2F Lanting Road, Binjiang District, Hangzhou City,</text>
      <text x="398" y="553">Zhejiang Prov. China 310000</text>
      <text x="398" y="560" font-size="4.2">☎ 0571-80041270 / ▯ 0571-80041271 / ✉ office@norvale.example</text>
    </g>

    <g class="envelope-back" fill="var(--paper)" stroke="var(--line)" stroke-width="0.8">
      <rect x="622" y="377" width="250" height="178" rx="8"/>
      <path d="M622 431 L872 431" fill="none"/>
      <path d="M624 433 L638 452 L856 452 L870 433" fill="none"/>
      <path d="M638 452 L632 530 M856 452 L862 530" fill="none"/>
    </g>
    <g font-size="3.8" fill="var(--text-dark)" font-family="Didact Gothic, sans-serif">
      <text x="740" y="534">Norvale Textiles Co., Ltd. Hangzhou</text>
      <text x="740" y="539">No.18 2F Lanting Road, Binjiang District, Hangzhou City,</text>
      <text x="740" y="544">Zhejiang Prov. China 310000</text>
      <text x="740" y="551" font-size="4.2">☎ 0571-80041270 / ▯ 0571-80041271 / ✉ office@norvale.example</text>
    </g>
  </svg>

  <div class="palette-title">COLOR :</div>
  <div class="swatch swatch-white">C:0 M:0 Y:0 K:0</div>
  <div class="swatch swatch-black">C:0 M:0 Y:0 K:100</div>
  <div class="swatch swatch-blue">C:63 M:0 Y:0 K:100</div>
  <div class="font-note">FONT : century gothic</div>

  <footer class="footer"></footer>
  <div class="footer-name">MARK VELLORAN</div>
</body>
</html>
```